Business needs Office Posters Designed

I need a office poster designed to put on a 2 feet x 3 feet space:
My Employee is Better Than Me.
- to signify the importance of listening to your employees, because they know better, more experienced in their respective fields.

Target Market(s)

employees

Industry/Entity Type

Healthcare

```html
<!DOCTYPE html>
<html lang="en">
<head>
<meta charset="utf-8">
<title>My Employee Is Better Than Me — Office Poster</title>
<link rel="stylesheet" href="https://fonts.googleapis.com/css2?family=Bebas+Neue&display=swap">
<style>
  :root {
    --indigo: #4a4fa8;
    --violet: #7a6a9c;
    --mauve: #9a7a94;
    --apricot: #e0a07c;
    --white: #ffffff;
  }
  html, body {
    margin: 0;
    padding: 0;
    width: 801px;
    height: 1200px;
    overflow: hidden;
    background: var(--violet);
  }
  .poster {
    position: relative;
    width: 801px;
    height: 1200px;
    overflow: hidden;
  }
  .poster__backdrop {
    position: absolute;
    inset: 0;
    background:
      linear-gradient(150deg, rgba(74,79,168,0.55) 0%, rgba(74,79,168,0) 40%),
      linear-gradient(330deg, rgba(74,79,168,0.5) 0%, rgba(74,79,168,0) 35%),
      radial-gradient(circle at 30% 35%, rgba(224,160,124,0.55) 0%, rgba(224,160,124,0) 40%),
      radial-gradient(circle at 80% 55%, rgba(224,160,124,0.45) 0%, rgba(224,160,124,0) 35%),
      radial-gradient(circle at 25% 80%, rgba(224,160,124,0.5) 0%, rgba(224,160,124,0) 38%),
      linear-gradient(180deg, var(--mauve) 0%, var(--violet) 50%, var(--mauve) 100%);
  }
  .poster__frame {
    position: absolute;
    left: 38px;
    top: 33px;
    width: 725px;
    height: 1132px;
    border: 2px solid var(--white);
    box-sizing: border-box;
  }
  .poster__headline {
    position: absolute;
    left: 118px;
    top: 122px;
    margin: 0;
    font-family: "Bebas Neue", "Oswald", sans-serif;
    font-weight: 400;
    font-size: 172px;
    line-height: 152px;
    letter-spacing: 1px;
    color: var(--white);
    text-shadow:
      -3px -2px 0 var(--indigo),
      -6px -4px 0 var(--apricot),
      -7px -5px 0 var(--white);
  }
  .poster__headline span {
    display: block;
  }
</style>
</head>
<body>
  <main class="poster">
    <div class="poster__backdrop" role="img" aria-label="Geometric hexagon pattern in indigo and apricot gradients"></div>
    <div class="poster__frame"></div>
    <h1 class="poster__headline">
      <span>My</span>
      <span>Employee</span>
      <span>Is</span>
      <span>Better</span>
      <span>Than</span>
      <span>Me</span>
    </h1>
  </main>
</body>
</html>
```